Flyer for a Payroll and Bookkeeping Companmy

Need a brochure to highlight our costs and service to hand out to clients.

Please see attachments for more information.

Industry/Entity Type

It Service

```html
<!DOCTYPE html>
<html lang="en">
<head>
<meta charset="utf-8">
<title>Harbor Ridge – Pricing Cards</title>
<link href="https://fonts.googleapis.com/css2?family=Montserrat:wght@300;400;500;600;700;800;900&display=swap" rel="stylesheet">
<style>
  :root{
    --blue:#1b74c5;
    --blue-dark:#0e5aa5;
    --orange:#e8761f;
    --frame:#b9babc;
    --ink:#333538;
    --ink-soft:#8a8c90;
    --pill:#3a3b3d;
    --rule:#c9cacc;
    --cell:#f4f4f5;
    --bg:#d9dadb;
  }
  *{box-sizing:border-box;margin:0;padding:0}
  html,body{width:1200px;height:998px;overflow:hidden}
  body{background:var(--bg);font-family:"Montserrat",sans-serif;color:var(--ink);position:relative}
  .card{position:absolute;left:247px;width:706px;height:470px;background:var(--blue);padding:9px}
  .card--payroll{top:19px}
  .card--bookkeeping{top:509px}
  .card__frame{width:100%;height:100%;background:var(--frame);padding:7px}
  .card__face{width:100%;height:100%;background:#fff;position:relative;overflow:hidden}

  .brand{position:absolute;right:26px;top:22px;display:flex;flex-direction:column;align-items:flex-end}
  .brand__name{display:flex;align-items:center;gap:8px;font-weight:700;font-size:26px;color:var(--blue-dark);letter-spacing:.2px}
  .brand__dot{width:16px;height:16px;border-radius:50%;background:var(--orange)}
  .brand__tag{font-weight:600;font-size:13px;color:var(--orange);margin-top:2px}

  /* payroll */
  .payroll__title{position:absolute;left:34px;top:44px;line-height:.95}
  .title__light{display:block;font-weight:300;color:var(--blue);font-size:40px;letter-spacing:1px}
  .title__bold{display:block;font-weight:900;color:var(--orange);font-size:52px;letter-spacing:1px}
  .payroll__offer{position:absolute;left:150px;top:200px;font-weight:900;font-size:44px;line-height:1.08;color:var(--pill);letter-spacing:.5px}
  .payroll__note{position:absolute;left:40px;right:40px;bottom:44px;background:var(--pill);border-radius:20px;padding:7px 22px;font-size:10px;font-weight:700;letter-spacing:.3px;color:#fff;line-height:1.45;text-align:right}
  .payroll__note em{font-style:normal;color:var(--orange)}
  .payroll__web{position:absolute;right:44px;bottom:16px;font-weight:800;font-size:12px;color:var(--pill)}

  /* bookkeeping */
  .books__title{position:absolute;left:44px;top:14px;line-height:.95}
  .books__title .title__light{font-size:30px}
  .books__title .title__bold{font-size:60px}
  .pricing{position:absolute;left:22px;top:104px;width:630px;border-collapse:collapse;border:2px solid var(--frame);font-size:10.5px}
  .pricing td,.pricing th{border:1px solid var(--rule);text-align:center;vertical-align:middle;height:30px;line-height:1.1}
  .pricing .svc-head{background:var(--blue-dark);color:#fff;font-weight:800;font-size:20px;text-align:center;width:210px}
  .tier__name{display:block;background:var(--orange);color:#fff;font-weight:800;font-size:8.5px;padding:3px 0;letter-spacing:.5px}
  .tier__price{display:block;background:var(--blue-dark);color:#fff;font-weight:800;font-size:15px;padding:2px 0 3px}
  .pricing th.tier{padding:0;width:105px;border-color:#fff}
  .pricing .label{text-align:right;padding-right:8px;font-weight:500;text-transform:uppercase;font-size:10.5px;background:#fff}
  .label small{display:block;font-size:8.5px;color:var(--ink-soft);font-weight:400;margin-top:1px}
  .pricing td.val{background:var(--cell);font-weight:500;text-transform:uppercase}
  .freq{color:var(--orange);font-weight:500;display:block;margin-top:1px}
  .tick{width:15px;height:10px;display:block;margin:0 auto}
  .cross{color:var(--orange);font-weight:700;font-size:17px;line-height:1}
  .money{color:var(--orange);font-weight:500;display:block;margin-top:1px}
  .books__footer{position:absolute;left:0;right:0;bottom:12px;text-align:center;font-weight:800;font-size:11.5px;color:var(--pill)}
</style>
</head>
<body>
<svg width="0" height="0" style="position:absolute" aria-hidden="true">
  <symbol id="tick" viewBox="0 0 16 11"><path d="M1.5 5.5 L6 9.5 L14.5 1.5" fill="none" stroke="#e8761f" stroke-width="2.4" stroke-linecap="round" stroke-linejoin="round"/></symbol>
</svg>

<section class="card card--payroll">
  <div class="card__frame"><div class="card__face">
    <h1 class="payroll__title"><span class="title__light">SIMPLIFIED</span><span class="title__bold">PAYROLL</span><span class="title__bold">PRICING</span></h1>
    <div class="brand"><span class="brand__name"><span class="brand__dot"></span>Harbor Ridge</span><span class="brand__tag">Payroll and Bookkeeping</span></div>
    <p class="payroll__offer">$25 PER PAYROLL<br>+$5 PER EMPLOYEE<br>NO SET UP FEES!</p>
    <p class="payroll__note">+$10 IF YOU ELECT TO HAVE PAPER CHECKS SHIPPED TO YOU.<br><em>*$5 PER EMPLOYEE DROPS TO $4 AFTER 20 EMPLOYEES.</em></p>
    <p class="payroll__web">HARBORRIDGE.COM</p>
  </div></div>
</section>

<section class="card card--bookkeeping">
  <div class="card__frame"><div class="card__face">
    <h1 class="books__title"><span class="title__light">BOOKKEEPING</span><span class="title__bold">PRICING</span></h1>
    <div class="brand"><span class="brand__name"><span class="brand__dot"></span>Harbor Ridge</span><span class="brand__tag">Payroll and Bookkeeping</span></div>
    <table class="pricing">
      <thead>
        <tr>
          <th class="svc-head">SERVICES</th>
          <th class="tier"><span class="tier__name">PREMIUM</span><span class="tier__price">$999</span></th>
          <th class="tier"><span class="tier__name">ENTREPRENEUR</span><span class="tier__price">$599</span></th>
          <th class="tier"><span class="tier__name">GROWTH</span><span class="tier__price">$299</span></th>
          <th class="tier"><span class="tier__name">START UP</span><span class="tier__price">$149</span></th>
        </tr>
      </thead>
      <tbody>
        <tr><td class="label">Employees</td><td class="val">Around<br>10+</td><td class="val">Around<br>5-9</td><td class="val">Around<br>2-5</td><td class="val">Around<br>1-2</td></tr>
        <tr><td class="label">Transactions / Month</td><td class="val">Up to<br>250</td><td class="val">Up to<br>150</td><td class="val">Up to<br>75</td><td class="val">Up to<br>50</td></tr>
        <tr><td class="label">Bookkeeping</td><td class="val"><svg class="tick"><use href="#tick"/></svg><span class="freq">Weekly</span></td><td class="val"><svg class="tick"><use href="#tick"/></svg><span class="freq">Weekly</span></td><td class="val"><svg class="tick"><use href="#tick"/></svg><span class="freq">Monthly</span></td><td class="val"><svg class="tick"><use href="#tick"/></svg><span class="freq">Quarterly</span></td></tr>
        <tr><td class="label">Financial Reports &amp; Review</td><td class="val"><svg class="tick"><use href="#tick"/></svg><span class="freq">Monthly</span></td><td class="val"><svg class="tick"><use href="#tick"/></svg><span class="freq">Monthly</span></td><td class="val"><svg class="tick"><use href="#tick"/></svg><span class="freq">Monthly</span></td><td class="val"><svg class="tick"><use href="#tick"/></svg><span class="freq">Quarterly</span></td></tr>
        <tr><td class="label">Support<small>(Phone and Chat)</small></td><td class="val"><svg class="tick"><use href="#tick"/></svg></td><td class="val"><svg class="tick"><use href="#tick"/></svg></td><td class="val"><svg class="tick"><use href="#tick"/></svg></td><td class="val"><svg class="tick"><use href="#tick"/></svg></td></tr>
        <tr><td class="label">Online Collaboration Portal<small>(Shared Folder)</small></td><td class="val"><svg class="tick"><use href="#tick"/></svg></td><td class="val"><svg class="tick"><use href="#tick"/></svg></td><td class="val"><svg class="tick"><use href="#tick"/></svg></td><td class="val"><svg class="tick"><use href="#tick"/></svg></td></tr>
        <tr><td class="label">Business Tax Return</td><td class="val"><svg class="tick"><use href="#tick"/></svg></td><td class="val"><svg class="tick"><use href="#tick"/></svg></td><td class="val">$799</td><td class="val">$599</td></tr>
        <tr><td class="label">Bill Pay<small>(With approval process)</small></td><td class="val"><svg class="tick"><use href="#tick"/></svg><span class="money">$5 / PAYMENT</span></td><td class="val"><span class="cross">×</span></td><td class="val"><span class="cross">×</span></td><td class="val"><span class="cross">×</span></td></tr>
      </tbody>
    </table>
    <p class="books__footer">1820 W MAPLE AVE, RIVERTON, UT 84065 &nbsp;•&nbsp; 555-014-2290 &nbsp;•&nbsp; HARBORRIDGE.COM</p>
  </div></div>
</section>
</body>
</html>
```